Bref créative
Holy Brambleton Chapel Stationary
Fr. Gerald Brint
Professional
pastor
415 Pinecrest Dr. West
Oakville, ON K2R 8W4
pastor@hbcvx.ca
www.hbcvx.ca
I think the Letterhead will work better is offset to the right corner so that the left side of the page could still be used for typing date, address, etc.. However, open to other ideas.
use map provided in download section. I will try to get the ai file shortly.
The wave is okay, but it cannot touch the edge of the paper.
Please use the map in the top left corner. Thx

```html
<!DOCTYPE html>
<html lang="en">
<head>
<meta charset="utf-8">
<title>Holy Brambleton Chapel Stationery</title>
<link href="https://fonts.googleapis.com/css2?family=Cinzel:wght@400;600&family=Open+Sans:wght@400;600&display=swap" rel="stylesheet">
<style>
:root{
  --bg:#e4e4e4;
  --paper:#ffffff;
  --brown:#5b4a42;
  --brown-light:#8a7a70;
  --ghost:#f1efee;
  --label:#555555;
}
*{margin:0;padding:0;box-sizing:border-box}
html,body{width:1200px;height:514px;overflow:hidden;background:var(--bg);font-family:"Open Sans",sans-serif}
.canvas{position:relative;width:1200px;height:514px}
.sheet{position:absolute;background:var(--paper);box-shadow:0 1px 3px rgba(0,0,0,.25);overflow:hidden}
.label{position:absolute;font-size:6px;color:var(--label);text-align:center;width:100%;top:-10px}
.item{position:absolute}
.letterhead{width:247px;height:372px;top:120px}
.lh-1{left:29px}.lh-2{left:307px}.lh-3{left:583px}
.ghost-mark{position:absolute;left:38px;top:150px;width:170px;height:120px;
  background:linear-gradient(180deg,var(--ghost),#f6f5f4);border-radius:60px 60px 0 0}
.wave{position:absolute;left:0;bottom:0;width:100%;height:50px}
.brand{font-family:"Cinzel",serif;font-weight:600;color:var(--brown);display:flex;align-items:center;gap:3px;white-space:nowrap}
.brand .dot{width:5px;height:5px;background:var(--brown);flex:none}
.brand.sm{font-size:5px}
.brand.md{font-size:6.5px}
.lh-head{position:absolute;right:14px;top:14px}
.lh-foot-brand{position:absolute;right:10px;bottom:8px;color:#fff}
.lh-foot-brand .dot{background:#fff}
.lh-foot-brand.brand{color:#fff}
.lh-contact{position:absolute;right:14px;bottom:52px;font-size:3.5px;line-height:5px;color:var(--brown);text-align:right}
.card{width:84px;height:43px;top:41px}
.card-front{left:619px;display:flex;align-items:center;justify-content:center;flex-direction:column;gap:3px}
.card-front .person{font-size:3.5px;color:var(--brown-light)}
.card-back{left:713px;background:var(--brown)}
.card-back .map{position:absolute;left:6px;top:5px;width:46px;height:33px;border:1px solid #cbbfb8;border-radius:50%;background:rgba(255,255,255,.08)}
.card-back .info{position:absolute;right:5px;top:10px;font-size:3.3px;line-height:4.6px;color:#fff;text-align:right}
.envelope{width:300px;height:138px;left:864px}
.env-1{top:30px}.env-2{top:189px}.env-3{top:348px;height:144px}
.env-brand{position:absolute;left:18px;top:16px}
.env-addr{position:absolute;left:18px;top:30px;font-size:3.5px;color:var(--brown-light)}
.env-flap{position:absolute;left:0;top:0;width:100%;height:100%}
.env-center{position:absolute;left:50%;top:56px;transform:translateX(-50%)}
</style>
</head>
<body>
<div class="canvas">

  <!-- Letterhead option 1 -->
  <div class="sheet letterhead lh-1">
    <div class="ghost-mark" role="img" aria-label="Faint church building illustration"></div>
    <svg class="wave" viewBox="0 0 247 50" preserveAspectRatio="none">
      <path d="M0 22 Q70 4 130 20 T247 14 L247 50 L0 50Z" fill="var(--brown)"/>
      <path d="M0 18 Q70 0 130 16 T247 10" fill="none" stroke="var(--brown-light)" stroke-width="1"/>
    </svg>
    <div class="brand sm lh-foot-brand"><span class="dot"></span>Holy Brambleton Chapel</div>
  </div>
  <div class="item" style="left:29px;top:120px;width:247px"><div class="label">Letterhead - Option 1</div></div>

  <!-- Letterhead option 2 -->
  <div class="sheet letterhead lh-2">
    <div class="brand md lh-head"><span class="dot"></span>Holy Brambleton Chapel</div>
    <div class="ghost-mark" role="img" aria-label="Faint church building illustration"></div>
    <div class="lh-contact">Fr. Gerald Brint<br>415 Pinecrest Dr. West<br>Oakville, ON K2R 8W4</div>
    <svg class="wave" viewBox="0 0 247 50" preserveAspectRatio="none">
      <path d="M0 26 Q80 6 140 22 T247 16 L247 50 L0 50Z" fill="var(--brown)"/>
      <path d="M0 22 Q80 2 140 18 T247 12" fill="none" stroke="var(--brown-light)" stroke-width="1"/>
    </svg>
  </div>
  <div class="item" style="left:307px;top:120px;width:247px"><div class="label">Letterhead - Option 2</div></div>

  <!-- Letterhead option 3 -->
  <div class="sheet letterhead lh-3">
    <div class="brand md lh-head"><span class="dot"></span>Holy Brambleton Chapel</div>
    <div class="ghost-mark" role="img" aria-label="Faint church building illustration"></div>
    <div class="lh-contact">pastor@hbcvx.ca<br>www.hbcvx.ca</div>
    <svg class="wave" viewBox="0 0 247 50" preserveAspectRatio="none">
      <path d="M0 30 Q90 8 150 24 T247 18 L247 50 L0 50Z" fill="var(--brown)"/>
      <path d="M0 26 Q90 4 150 20 T247 14" fill="none" stroke="var(--brown-light)" stroke-width="1"/>
    </svg>
  </div>
  <div class="item" style="left:583px;top:120px;width:247px"><div class="label">Letterhead - Option 3</div></div>

  <!-- Business cards -->
  <div class="sheet card card-front">
    <div class="brand sm"><span class="dot"></span>Holy Brambleton Chapel</div>
    <div class="person">Fr. Gerald Brint · pastor</div>
  </div>
  <div class="item" style="left:619px;top:41px;width:84px"><div class="label">Business Card Front</div></div>

  <div class="sheet card card-back">
    <div class="map" role="img" aria-label="Location map of the chapel"></div>
    <div class="info">415 Pinecrest Dr. West<br>Oakville, ON K2R 8W4<br>pastor@hbcvx.ca<br>www.hbcvx.ca</div>
  </div>
  <div class="item" style="left:713px;top:41px;width:84px"><div class="label">Business Card Back</div></div>

  <!-- Envelopes -->
  <div class="sheet envelope env-1">
    <div class="brand md env-brand"><span class="dot"></span>Holy Brambleton Chapel</div>
  </div>
  <div class="item" style="left:864px;top:30px;width:300px"><div class="label">Envelope - Option 1</div></div>

  <div class="sheet envelope env-2">
    <div class="brand md env-brand"><span class="dot"></span>Holy Brambleton Chapel</div>
    <div class="env-addr">415 Pinecrest Dr. West, Oakville, ON K2R 8W4</div>
  </div>
  <div class="item" style="left:864px;top:189px;width:300px"><div class="label">Envelope - Option 2</div></div>

  <div class="sheet envelope env-3">
    <svg class="env-flap" viewBox="0 0 300 144" preserveAspectRatio="none">
      <path d="M0 0 L150 88 L300 0" fill="none" stroke="#d6d2cf" stroke-width="1"/>
      <path d="M0 144 L125 70 M300 144 L175 70" fill="none" stroke="#e2dfdd" stroke-width="1"/>
    </svg>
    <div class="brand sm env-center"><span class="dot"></span>Holy Brambleton Chapel</div>
  </div>
  <div class="item" style="left:864px;top:348px;width:300px"><div class="label">Envelope Back</div></div>

</div>
</body>
</html>
```